Protein Powder Product Label Design

We are going to launch Protein Powder Product shortly and looking for the Unique, Attractive and Best Product label Design. The label size should be 5.5x17.

Here are some competitors label design which I like the most:
https://trelquo.com/collections/daily-nutrition/products/dorn-pax-organic?variant=48201937561420 (Like the way it described each nutrition element at the bottom & Flavors Image)
https://www.quimbrix.com/products/calmrise-stress-anxiety-relief (Like the Logo on Side)
www.7xq.ord (Overall Designs & Color Combination)

I have attached Generic Product Label design template so that you can have all the content required for the label.

Target Market(s)

Nutrition, Sport Nutrition, Protein Powder

Industry/Entity Type

Nutrition

Font styles to use
Sans Serif

Requirements
Must have
• 1. Follows proper Label Guidelines
2. Within Given Label Dimensions
3. Attractive & Unique Label Designs
4. Excellent Color Combinations
Nice to have
• My Product containers will a Black Color Tub. Adjust the label background color accordingly so that it looks attractive.
Should not have
• Exact Label designs for any existing products

```html
<!DOCTYPE html>
<html lang="en">
<head>
<meta charset="UTF-8">
<title>Vegan Chocolate Milkshake Label</title>
<link rel="stylesheet" href="https://fonts.googleapis.com/css2?family=Oswald:wght@500;600;700&display=swap">
<style>
  :root {
    --page: #f3f3f3;
    --label-black: #050505;
    --lime: #c9d22b;
    --lime-deep: #a9b437;
    --slate: #2c333a;
    --slate-light: #3a424a;
    --white: #ffffff;
    --cocoa-dark: #4a2616;
    --cocoa: #7b4a2e;
    --cocoa-light: #a56a44;
  }
  html, body {
    margin: 0;
    width: 993px;
    height: 1200px;
    overflow: hidden;
    background: var(--page);
  }
  .label {
    position: absolute;
    left: 30px;
    top: 178px;
    width: 933px;
    height: 843px;
    display: block;
  }
  .label-text { font-family: "Oswald", sans-serif; }
  .title { font-weight: 600; fill: var(--white); }
  .flavor-tag { font-weight: 500; fill: var(--label-black); }
  .claim { font-weight: 600; fill: var(--white); }
  .variant { font-weight: 500; fill: var(--label-black); }
  .net-weight { font-weight: 600; fill: var(--lime); }
</style>
</head>
<body>
<svg class="label" viewBox="0 0 830 750" xmlns="http://www.w3.org/2000/svg">
  <defs>
    <linearGradient id="lime-band" x1="0" y1="0" x2="1" y2="0">
      <stop offset="0" stop-color="var(--lime-deep)"/>
      <stop offset="0.8" stop-color="var(--lime-deep)"/>
      <stop offset="0.8" stop-color="var(--lime)"/>
      <stop offset="1" stop-color="var(--lime)"/>
    </linearGradient>
    <radialGradient id="cocoa-splash" cx="0.5" cy="0.6" r="0.55">
      <stop offset="0" stop-color="var(--cocoa-light)"/>
      <stop offset="0.6" stop-color="var(--cocoa)"/>
      <stop offset="1" stop-color="var(--cocoa-dark)"/>
    </radialGradient>
  </defs>

  <rect class="label-base" width="830" height="750" fill="var(--label-black)"/>

  <polygon class="accent-lime-left" points="0,0 50,0 0,220" fill="var(--lime-deep)"/>
  <polygon class="accent-slate-top" points="645,0 830,0 830,90 795,240" fill="var(--slate)"/>
  <polygon class="accent-slate-top-inner" points="700,0 760,0 830,70 830,90" fill="var(--slate-light)"/>
  <polygon class="accent-lime-right" points="825,80 830,80 830,750 685,750" fill="url(#lime-band)"/>
  <polygon class="accent-slate-bottom" points="0,600 85,745 0,745" fill="var(--slate)"/>

  <text class="label-text title" x="55" y="320" font-size="270" textLength="585" lengthAdjust="spacingAndGlyphs">VEGAN</text>

  <polygon class="flavor-tag-box" points="70,362 465,362 445,450 70,450" fill="var(--white)"/>
  <text class="label-text flavor-tag" x="87" y="428" font-size="64" textLength="340" lengthAdjust="spacingAndGlyphs">Natural Flavor</text>

  <text class="label-text claim" x="87" y="520" font-size="58" textLength="173" lengthAdjust="spacingAndGlyphs">DIETARY</text>
  <text class="label-text claim" x="87" y="582" font-size="58" textLength="268" lengthAdjust="spacingAndGlyphs">SUPPLEMENT</text>

  <rect class="variant-band" x="68" y="590" width="372" height="80" fill="var(--lime)"/>
  <text class="label-text variant" x="87" y="648" font-size="44" textLength="315" lengthAdjust="spacingAndGlyphs">CHOCOLATE MILKSHAKE</text>

  <text class="label-text net-weight" x="85" y="725" font-size="32" textLength="215" lengthAdjust="spacingAndGlyphs">Net Wt. 907 G (2LB)</text>

  <ellipse class="flavor-illustration" cx="600" cy="560" rx="170" ry="190" fill="url(#cocoa-splash)" role="img" aria-label="Chocolate pieces with a chocolate and milk splash"/>
</svg>
</body>
</html>
```